Web Design Project for Film Business

We need a web design for a new company based in Bondi Beach, Sydney, Australia. We basically provide filming and video editing services. Our targets are basically corporate videos, wedding videos and other types of functions.
The important thing to know about us is that we are not just people that press the record button, we consider ourselves story tellers. We can make something boring like a conference look interesting to watch and we can also make a wedding look like a blockbuster movie that you can't look away from until its finished.
We need something as new and fresh as Bondi Beach. A young place where people come from all over the world to enjoy summer and we are lucky to be based here.
To see some of our work please visit our tavlora Channel. Make sure you watch a couple of wedding video and the corporate video so you can have a better understanding about our style.
Please note- we are not trying to market ourselves exclusively as wedding videographers, nor do we want to exploit the idea of the beach.

http://tavlora.com/channels/815374

sites that we really like:

http://www.quillpathreels.co.uk/
http://www.marnowebb.co.uk/

Target Market(s)

Couples - Corporate

Industry/Entity Type

Business

Requirements
Must have
• 5 to 6 pages (we are still deciding)
-main page
-our story (story about Karrow Films)
-your story (page designated for wedding videos)
-your business (page designated for corporate videos)
-contact us
-other stuff
Nice to have
• I would like to see some animation. Maybe you can animate our logo. Up to the designer

```html
<!DOCTYPE html>
<html lang="en">
<head>
<meta charset="utf-8">
<title>Karrow Films</title>
<link rel="stylesheet" href="https://fonts.googleapis.com/css2?family=Arimo:ital,wght@0,400;0,700;1,400&display=swap">
<style>
:root{
  --ink:#0f1114;
  --header:#121315;
  --hero-light:#33373d;
  --hero-dark:#15181d;
  --cyan:#1eb0d3;
  --white:#ffffff;
  --muted:#9a9ea4;
  --footer:#c9c9c9;
  --footer-text:#141414;
}
*{box-sizing:border-box;margin:0;padding:0}
html,body{width:1191px;height:1200px;overflow:hidden}
body{position:relative;font-family:"Arimo",Arial,sans-serif;background:var(--hero-dark);color:var(--white)}
.abs{position:absolute}

/* Header */
.site-header{left:0;top:0;width:1191px;height:115px;background:linear-gradient(#0c0d0f,#1a1b1e)}
.brand{left:183px;top:20px;font-weight:700;font-size:40px;line-height:39px;letter-spacing:1px;color:var(--white);text-transform:uppercase}
.brand .line2{display:block;padding-left:7px}
.nav{left:478px;top:84px;display:flex;list-style:none}
.nav li{font-size:11.5px;font-weight:700;letter-spacing:.3px;padding:0 8px;height:27px;line-height:18px;border-left:1px solid #2c2e31;white-space:nowrap}
.nav li:first-child{border-left:none}
.nav-pointer{left:495px;top:115px;width:0;height:0;border-left:6px solid transparent;border-right:6px solid transparent;border-top:6px solid #121315}
.badge-new{left:920px;top:51px;width:54px;height:22px;background:var(--cyan);color:var(--white);font-weight:700;font-size:13px;line-height:22px;text-align:center;clip-path:polygon(0 0,100% 0,92% 100%,8% 100%)}

/* Hero */
.hero{left:0;top:115px;width:1191px;height:795px;background:radial-gradient(ellipse 700px 420px at 470px 200px,var(--hero-light),var(--hero-dark) 80%)}
.hero-title{left:198px;top:160px;font-size:53px;font-weight:700;line-height:60px}
.hero-sub{left:198px;top:220px;font-size:33px;line-height:41px;width:400px}
.hero-text{left:197px;top:319px;width:362px;font-size:13.2px;line-height:16.5px;color:#e8e8e8}
.btn-ribbon{left:198px;top:410px;width:239px;height:21px;background:var(--cyan);color:var(--ink);font-weight:700;font-size:13px;line-height:21px;padding-left:8px;clip-path:polygon(0 0,100% 0,96% 100%,0 100%)}
.hero-art{left:650px;top:168px;width:328px;height:267px;border-radius:50%;background:radial-gradient(circle at 35% 45%,#1eb0d3 0,#1a8fab 30%,rgba(200,210,220,.25) 55%,rgba(0,0,0,0) 72%)}

/* Cards */
.card-photo{top:517px;width:190px;height:147px;border:2px solid var(--white)}
.photo-couple{background:linear-gradient(160deg,#c9c4bc,#8a8f96 50%,#4d6a7a)}
.photo-beach{background:linear-gradient(160deg,#6b4e33,#b98a5d 55%,#7a5636)}
.photo-guitar{background:linear-gradient(135deg,#6b5444,#d2a57e 50%,#8c6a55)}
.photo-conference{background:linear-gradient(110deg,#1d1f22 40%,#8ea2ac 70%,#c8d2d8)}
.card-title{top:686px;width:190px;height:22px;background:var(--cyan);color:var(--ink);font-weight:700;font-size:13px;line-height:23px;padding-left:4px;white-space:nowrap;clip-path:polygon(0 0,100% 0,95% 100%,0 100%)}
.card-text{top:718px;width:192px;font-size:11.4px;line-height:13.7px;color:var(--muted);padding-left:4px}
.read-more{color:var(--cyan);font-style:italic}

/* Footer */
.edge{left:0;top:902px}
.site-footer{left:0;top:910px;width:1191px;height:290px;background:var(--footer);color:var(--footer-text)}
.foot-col{top:45px}
.foot-col h3{font-size:14px;font-weight:700;margin-bottom:11px;white-space:nowrap}
.foot-col ul{list-style:none}
.foot-col li{font-size:11.4px;height:25.3px;padding-left:13px;position:relative}
.foot-col li::before{content:"";position:absolute;left:1px;top:3px;border-top:3.5px solid transparent;border-bottom:3.5px solid transparent;border-left:4px solid var(--footer-text)}
.social{left:858px;top:24px;display:grid;grid-template-columns:72px 72px;row-gap:8px;list-style:none}
.social li{font-size:11px;display:flex;align-items:center;gap:5px}
.social li span{display:inline-block;width:10px;height:10px;background:var(--cyan)}
.copyright{left:172px;top:235px;width:191px;height:22px;background:var(--cyan);color:var(--white);font-size:10.5px;font-weight:700;line-height:22px;padding-left:8px;clip-path:polygon(0 0,100% 0,95% 100%,0 100%)}
</style>
</head>
<body>

<header class="site-header abs">
  <div class="brand abs">Karrow<span class="line2">Films</span></div>
  <ul class="nav abs">
    <li>HOME</li>
    <li>OUR STORY</li>
    <li>YOUR STORY</li>
    <li>YOUR BUSINESS</li>
    <li>CONTACT US</li>
    <li>OTHER STUFF</li>
  </ul>
  <div class="badge-new abs">NEW</div>
</header>

<section class="hero abs">
  <h1 class="hero-title abs" style="top:45px">Lorem ipsum</h1>
  <p class="hero-sub abs" style="top:105px">Dolor sit amet, conse tetuer dolor sit amet</p>
  <p class="hero-text abs" style="top:204px">Adipiscing elit. Aenean commodo ligula eget dolor. Aenean massa. Aum sociis natoque penatibus et magnis dis parturient montes, nascetur ridiculus mus. Donec quam felis, ultricies nec, pellentesque eu, pretium quis.</p>
  <div class="btn-ribbon abs" style="top:295px">Aenean commodo ligul aeget</div>
  <div class="hero-art abs" style="top:50px" role="img" aria-label="Illustration of stacked film canisters and an unspooling film reel"></div>

  <div class="card-photo photo-couple abs" style="left:177px;top:402px" role="img" aria-label="Photo of a couple by the water"></div>
  <div class="card-photo photo-beach abs" style="left:389px;top:402px" role="img" aria-label="Photo of a surfer walking on the beach"></div>
  <div class="card-photo photo-guitar abs" style="left:602px;top:402px" role="img" aria-label="Photo of hands playing an acoustic guitar"></div>
  <div class="card-photo photo-conference abs" style="left:815px;top:402px" role="img" aria-label="Photo of a conference venue foyer"></div>

  <h2 class="card-title abs" style="left:177px;top:571px">Maecenas nec odio et ante</h2>
  <h2 class="card-title abs" style="left:391px;top:571px">Maecenas nec odio et ante</h2>
  <h2 class="card-title abs" style="left:603px;top:571px">Maecenas nec odio et ante</h2>
  <h2 class="card-title abs" style="left:817px;top:571px">Maecenas nec odio et ante</h2>

  <p class="card-text abs" style="left:177px;top:603px">Tincidunt tempus donec vitae sapien ut libero venenatis faucibus. Nullam quis ante. Etiam sit amet orci eget eros faucibus tincidunt. Duis leo. Sed fringilla mauris sit amet nibh. Donec sodales sagittis magna. Sed consequat, leo eget bibendum sodales, augue velit cursus <span class="read-more">Read More...</span></p>
  <p class="card-text abs" style="left:391px;top:603px">Tincidunt tempus donec vitae sapien ut libero venenatis faucibus. Nullam quis ante. Etiam sit amet orci eget eros faucibus tincidunt. Duis leo. Sed fringilla mauris sit amet nibh. Donec sodales sagittis magna. Sed consequat, leo eget bibendum sodales, augue velit cursus nunc <span class="read-more">Read More...</span></p>
  <p class="card-text abs" style="left:603px;top:603px">Tincidunt tempus donec vitae sapien ut libero venenatis faucibus. Nullam quis ante. Etiam sit amet orci eget eros faucibus tincidunt. Duis leo. Sed fringilla mauris sit amet nibh. Donec sodales sagittis magna. Sed consequat, leo eget bibendum sodales, augue velit cursus nunc<span class="read-more">Read More...</span></p>
  <p class="card-text abs" style="left:817px;top:603px">Tincidunt tempus donec vitae sapien ut libero venenatis faucibus. Nullam quis ante. Etiam sit amet orci eget eros faucibus tincidunt. Duis leo. Sed fringilla mauris sit amet nibh. Donec sodales sagittis magna. Sed consequat, leo eget bibendum sodales, augue velit cursus nunc<span class="read-more">Read More...</span></p>
</section>

<div class="nav-pointer abs"></div>

<svg class="edge abs" width="1191" height="9" viewBox="0 0 1191 9" aria-hidden="true">
  <defs>
    <pattern id="teeth" width="8" height="9" patternUnits="userSpaceOnUse">
      <polygon points="0,9 4,2 8,9" fill="#c9c9c9"/>
    </pattern>
  </defs>
  <rect width="1191" height="9" fill="url(#teeth)"/>
</svg>

<footer class="site-footer abs">
  <div class="foot-col abs" style="left:177px">
    <h3>Maecenas nec odio et ante</h3>
    <ul><li>Tincidunt tempus donec</li><li>Vitae sapien ut libero</li><li>Venenatis faucibus</li><li>Nullam quis ante</li><li>Etiam sit amet orcic</li></ul>
  </div>
  <div class="foot-col abs" style="left:395px">
    <h3>Maecenas nec odio et ante</h3>
    <ul><li>Tincidunt tempus donec</li><li>Vitae sapien ut libero</li><li>Venenatis faucibus</li><li>Nullam quis ante</li><li>Etiam sit amet orcic</li></ul>
  </div>
  <div class="foot-col abs" style="left:613px">
    <h3>Maecenas nec odio et ante</h3>
    <ul><li>Tincidunt tempus donec</li><li>Vitae sapien ut libero</li><li>Venenatis faucibus</li><li>Nullam quis ante</li><li>Etiam sit amet orcic</li></ul>
  </div>
  <ul class="social abs">
    <li><span></span>Skylark</li>
    <li><span></span>Gatherly</li>
    <li><span></span>tavlora</li>
    <li><span></span>Snapfield</li>
  </ul>
  <div class="copyright abs">© Copyright 2011 KARROW FILMS</div>
</footer>

</body>
</html>
```